Marlowe Business Partners Business Card

I'd Like a Two sided Card. Logo was uploaded as an EPS. If you need an additional type, let me know. Colors in Logo are Pantone 289C and Pantone 348C.

I'm thinking of raising the Print on the front, if that matters. Also would like any Vector Art used in the design included with the uploaded files when awarded. If you need any additional info, please let me know. Uploaded card design was for informational purposes only.

The back of the card should be blue, and I like the design included for the back.
Updates

On the Back of the Card, I will probably want my web address. (www.marlowebusinesspartners.example)

Only Square Card Designs Please

Industry/Entity Type

Business

Requirements
Must have
• Should have enough room for longer email addresses in the future.
Nice to have
• email address above WEb URL.

```html
<!DOCTYPE html>
<html lang="en">
<head>
<meta charset="utf-8">
<title>Marlowe Business Partners – Business Card</title>
<link rel="stylesheet" href="https://fonts.googleapis.com/css2?family=Open+Sans:wght@400;600;700&display=swap">
<style>
  :root {
    --navy: #0c2340;
    --navy-deep: #071629;
    --navy-soft: #16325a;
    --green: #00843d;
    --paper: #ffffff;
    --stage: #e4e4e4;
    --rule: rgba(255,255,255,0.16);
    --ink-light: #ffffff;
    --ink-muted: #c9d3e0;
  }
  * { box-sizing: border-box; margin: 0; padding: 0; }
  html, body { width: 1200px; height: 1129px; overflow: hidden; }
  body {
    background: var(--stage);
    font-family: "Open Sans", Arial, sans-serif;
    position: relative;
  }
  .card {
    position: absolute;
    top: 304px;
    width: 520px;
    height: 520px;
    box-shadow: 0 2px 10px rgba(0,0,0,0.18);
    overflow: hidden;
  }
  .card--front { left: 50px; background: var(--paper); }
  .card--back { left: 630px; display: flex; flex-direction: column; background: var(--navy); }

  .mark-square { background: var(--navy); flex: none; }

  /* Front: wordmark set vertically */
  .front-mark {
    position: absolute;
    left: 50%;
    top: 50%;
    transform: translate(-50%, -50%) rotate(-90deg);
    display: flex;
    align-items: center;
    gap: 18px;
    white-space: nowrap;
  }
  .front-mark .mark-square { width: 44px; height: 44px; }
  .front-mark .wordmark {
    font-size: 34px;
    font-weight: 700;
    line-height: 1.15;
    color: var(--navy);
  }

  /* Back: header */
  .back-header {
    height: 96px;
    display: flex;
    align-items: center;
    justify-content: center;
    gap: 12px;
    background: var(--paper);
    flex: none;
  }
  .back-header .mark-square { width: 28px; height: 28px; }
  .back-header .wordmark {
    font-size: 23px;
    font-weight: 700;
    color: var(--navy);
    white-space: nowrap;
  }
  .header-rule {
    height: 6px;
    background: var(--navy-deep);
    position: relative;
    flex: none;
  }
  .header-rule::after {
    content: "";
    position: absolute;
    left: 0; top: 0;
    width: 62%;
    height: 3px;
    background: var(--green);
  }

  .back-body {
    flex: 1;
    background: linear-gradient(180deg, var(--navy-soft), var(--navy));
    display: flex;
    flex-direction: column;
    color: var(--ink-light);
  }
  .contact-row {
    height: 74px;
    display: flex;
    align-items: center;
    gap: 20px;
    padding: 0 30px;
    border-bottom: 1px solid var(--rule);
  }
  .contact-row:last-child { border-bottom: none; }
  .icon {
    width: 42px; height: 42px;
    border-radius: 50%;
    flex: none;
    display: flex; align-items: center; justify-content: center;
  }
  .icon--light { background: var(--paper); }
  .icon--green { background: var(--green); }
  .icon svg { width: 22px; height: 22px; }
  .person-name { font-size: 21px; font-weight: 700; line-height: 1.15; }
  .person-title { font-size: 15px; color: var(--ink-muted); }
  .contact-text { font-size: 16px; line-height: 1.35; }

  .back-footer {
    flex: none;
    height: 44px;
    background: radial-gradient(ellipse at 50% 40%, var(--navy), var(--navy-deep));
  }
</style>
</head>
<body>
  <section class="card card--front" aria-label="Card front">
    <div class="front-mark">
      <span class="mark-square"></span>
      <span class="wordmark">Marlowe Business<br>Partners, LLC</span>
    </div>
  </section>

  <section class="card card--back" aria-label="Card back">
    <header class="back-header">
      <span class="mark-square"></span>
      <span class="wordmark">Marlowe Business Partners, LLC</span>
    </header>
    <div class="header-rule"></div>

    <div class="back-body">
      <div class="contact-row">
        <span class="icon icon--light">
          <svg viewBox="0 0 24 24" fill="#0c2340"><circle cx="12" cy="8" r="4.5"/><path d="M3 21c0-5 4-8 9-8s9 3 9 8z"/></svg>
        </span>
        <div>
          <p class="person-name">ODALYS</p>
          <p class="person-title">Marketing Director</p>
        </div>
      </div>
      <div class="contact-row">
        <span class="icon icon--green">
          <svg viewBox="0 0 24 24" fill="none" stroke="#fff" stroke-width="2"><rect x="7" y="2.5" width="10" height="19" rx="1.5"/><line x1="10.5" y1="18.5" x2="13.5" y2="18.5"/></svg>
        </span>
        <p class="contact-text">(555) 014 2290</p>
      </div>
      <div class="contact-row">
        <span class="icon icon--light">
          <svg viewBox="0 0 24 24" fill="none" stroke="#0c2340" stroke-width="2"><rect x="3" y="6" width="18" height="12"/><path d="M3 6l9 7 9-7"/></svg>
        </span>
        <p class="contact-text">hello@marlowebp.example</p>
      </div>
      <div class="contact-row">
        <span class="icon icon--green">
          <svg viewBox="0 0 24 24" fill="none" stroke="#fff" stroke-width="1.8"><circle cx="12" cy="12" r="9"/><ellipse cx="12" cy="12" rx="4" ry="9"/><line x1="3" y1="12" x2="21" y2="12"/></svg>
        </span>
        <p class="contact-text">www.marlowebusinesspartners.example</p>
      </div>
      <div class="contact-row">
        <span class="icon icon--light">
          <svg viewBox="0 0 24 24" fill="#0c2340"><path d="M12 2a7 7 0 0 0-7 7c0 5 7 13 7 13s7-8 7-13a7 7 0 0 0-7-7zm0 9.5A2.5 2.5 0 1 1 12 6.5a2.5 2.5 0 0 1 0 5z"/></svg>
        </span>
        <p class="contact-text">PO Box 4410 Harbour Lane<br>East Marlowe 2210 Norland</p>
      </div>
    </div>

    <footer class="back-footer"></footer>
  </section>
</body>
</html>
```